Granite Ridge Holdings

I have a real estate investment business.

** I need editable vector files of the final design.

Industry/Entity Type

Real Estate

Contact Information for Business Card

I would like the card to be clear and direct with the company name and contact info. I would prefer not to have a design that is too busy (i.e., with excessive detail) in the business card.

Font styles to use
Sans Serif

Requirements
Must have
• My card must have the following information listed below:
• Company name: Grainite Ridge Holdings LLC
• My name: Daniel Vorsley
• Phone number: (555) 218-9067
• Email address: dtvorsley@mailbox-example.net
• Keywords: “Real Estate Investments”
Nice to have
• I would like to have a design that resembles the characteristics/uses of obsidian stone which resembles something related to strength and resilience. Perhaps something with sharp, sleek color transitions as well.

```html
<!DOCTYPE html>
<html lang="en">
<head>
<meta charset="utf-8">
<title>Grainite Ridge Holdings LLC – Business Card</title>
<link href="https://fonts.googleapis.com/css2?family=Roboto+Condensed:wght@400;700&display=swap" rel="stylesheet">
<style>
  :root {
    --page-bg: #ffffff;
    --card-bg: #fbfbfb;
    --navy: #2f3f58;
    --slate-violet: #6a719f;
    --ink: #3a3a3a;
  }
  html, body {
    margin: 0;
    padding: 0;
    width: 1200px;
    height: 1200px;
    overflow: hidden;
    background: var(--page-bg);
  }
  .business-card {
    position: absolute;
    left: 72px;
    top: 299px;
    width: 1056px;
    height: 602px;
    background: var(--card-bg);
    overflow: hidden;
  }
  .company-name {
    position: absolute;
    left: 56px;
    top: 120px;
    margin: 0;
    font-family: "Roboto Condensed", "Arial Narrow", sans-serif;
    font-weight: 700;
    font-size: 51px;
    line-height: 1;
    color: var(--navy);
  }
  .holder {
    position: absolute;
    left: 56px;
    top: 278px;
  }
  .holder-name {
    margin: 0;
    font-family: "Roboto Condensed", "Arial Narrow", sans-serif;
    font-weight: 700;
    font-size: 57px;
    line-height: 1;
    color: var(--slate-violet);
  }
  .holder-title {
    margin: 0;
    font-family: "Roboto Condensed", "Arial Narrow", sans-serif;
    font-weight: 400;
    font-size: 38px;
    line-height: 1;
    color: var(--ink);
  }
  .contact-list {
    position: absolute;
    left: 56px;
    top: 416px;
    margin: 0;
    padding: 0;
    list-style: none;
    font-family: "Roboto Condensed", "Arial Narrow", sans-serif;
    font-size: 31px;
    color: var(--ink);
  }
  .contact-item {
    display: flex;
    align-items: center;
    height: 40px;
  }
  .contact-icon {
    width: 24px;
    height: 24px;
    margin-right: 22px;
    fill: var(--slate-violet);
  }
  .tagline {
    position: absolute;
    right: 76px;
    top: 450px;
    margin: 0;
    font-family: "Roboto Condensed", "Arial Narrow", sans-serif;
    font-weight: 700;
    font-size: 35px;
    line-height: 1;
    color: var(--navy);
  }
  .footer-band {
    position: absolute;
    left: 0;
    bottom: 0;
    width: 1056px;
    height: 86px;
    background: linear-gradient(180deg, var(--slate-violet) 0%, var(--navy) 55%, var(--navy) 100%);
  }
</style>
</head>
<body>
  <article class="business-card">
    <h1 class="company-name">Grainite Ridge Holdings LLC</h1>

    <div class="holder">
      <p class="holder-name">Daniel Vorsley</p>
      <p class="holder-title">Manager</p>
    </div>

    <ul class="contact-list">
      <li class="contact-item">
        <svg class="contact-icon" viewBox="0 0 24 24" aria-hidden="true">
          <path d="M16 2 C18 2 20 4 19 5 L17 7 C16 8 14 7 13 7 C10 10 9 14 9 17 C10 17 11 16 12 17 L13 19 C13 21 11 22 9 22 C6 22 5 18 6 13 C7 8 11 2 16 2 Z"/>
        </svg>
        <span>(555) 218-9067</span>
      </li>
      <li class="contact-item">
        <svg class="contact-icon" viewBox="0 0 24 24" aria-hidden="true">
          <path d="M1 5 H23 V19 H1 Z M3 7 V17 L9 12 Z M21 7 L15 12 L21 17 Z M4 6.5 L12 13 L20 6.5 Z M4 17.5 H20 L14 13 L12 14.6 L10 13 Z"/>
        </svg>
        <span>dtvorsley@mailbox-example.net</span>
      </li>
    </ul>

    <p class="tagline">Real Estate Investments</p>

    <div class="footer-band" role="img" aria-label="Decorative layered wave band in slate violet and navy along the bottom edge"></div>
  </article>
</body>
</html>
```